Coffee Roastery Label Sticker Design

We are starting a small Micro-Coffee-Roastery and are looking for a catchy design, which might look a bit hipster style, but not too much. It's called "pebble kilnhouse", because we started roasting first in our backyard / garden by our house.
At the end of the logo and the details of the sticker (like all text elements) we need to be able to modify later by ourselfs. Coffee type, origin of coffee and so one ...
The label will be sticked on a white craftpaper coffee bag of 250grams. Sticker size around 8x12.5 cm.
The coffee bag should be an eye-catcher in a shop-shelve compared to the other coffee brands.
Another example that i really like (just to get you another idea of what we would love to get because we really like that style): https://pixvaultcdn.net/design_img/5719204/83051/61730482/qwmrlezt4k7b9d1pf2hyv8nusa_image.png).
OR https://packframe.net/blog/2016/3/14/larkhill-coffee?

Target Market(s)

"0Speciality Coffee" lovers
High quality specialty coffee and a clear origin of the bean and fair trade or project coffee is what makes our roasted coffee product special

Logo Text

Kiesel Brennerei

Requirements
Must have
• A house and a garden with either flowers or a tree is what we have in mind.
The printed label will be square 8x12.5 cm. We will use the logo on the printed label (we will print on our own printer) and on a homepage.
Nice to have
• In the attached logo example, there is no connection to a coffee business. Actually it would be a nice detail to include somehow either a descent coffee bean, a cup or a tiny roastery machine or whatever is in your mind with coffee ... (not a grinder)
Black and white is OK, but we also like colourfull very much
Please see the attached documents with sample designs that we created on our own with canvas. It's not too bad, but also a bit boring. If you have a completely different idea, please go for it. we are very open for other cool and hip designs or also quite descent and femail touch is fine too, but no must.

```html
<!DOCTYPE html>
<html lang="de">
<head>
<meta charset="utf-8">
<title>Kiesel Brennerei – Etiketten</title>
<link rel="stylesheet" href="https://fonts.googleapis.com/css2?family=Bebas+Neue&display=swap">
<style>
  :root {
    --canvas: #ececec;
    --label-bg: #ffffff;
    --frame: #3a4550;
    --ink: #27323d;
    --gold: #bf9f66;
    --rust: #d65a35;
    --umber: #8f4a0f;
    --on-accent: #ffffff;
  }
  * { box-sizing: border-box; margin: 0; padding: 0; }
  html, body { width: 1028px; height: 1200px; overflow: hidden; }
  body {
    background: var(--canvas);
    font-family: "Bebas Neue", "Arial Narrow", sans-serif;
    color: var(--ink);
  }
  .label-row {
    position: absolute;
    top: 358px;
    left: 25px;
    display: flex;
    gap: 34px;
  }
  .label {
    position: relative;
    width: 310px;
    height: 483px;
    background: var(--label-bg);
    border: 1.5px solid var(--frame);
  }
  .label--gold  { --accent: var(--gold); }
  .label--rust  { --accent: var(--rust); }
  .label--umber { --accent: var(--umber); }

  .brand-mark {
    position: absolute;
    top: 42px;
    left: 50%;
    width: 160px;
    height: 160px;
    margin-left: -80px;
    border-radius: 50%;
    background: var(--accent);
  }
  .brand-name {
    position: absolute;
    top: 222px;
    left: 0;
    width: 100%;
    text-align: center;
    font-size: 50px;
    line-height: 1;
    letter-spacing: 0.5px;
    color: var(--ink);
  }
  .product-band {
    position: absolute;
    top: 290px;
    left: 20px;
    width: 270px;
    height: 55px;
    background: var(--accent);
    color: var(--on-accent);
    text-align: center;
    font-size: 22px;
    line-height: 22px;
    padding-top: 6px;
  }
  .roast-level {
    position: absolute;
    top: 354px;
    left: 0;
    width: 100%;
    text-align: center;
    font-size: 12px;
    color: var(--accent);
  }
  .roast-level--dark { padding-left: 8px; }
  .bean-facts {
    position: absolute;
    top: 371px;
    right: 34px;
    text-align: right;
    font-size: 12.5px;
    line-height: 13.8px;
    list-style: none;
    color: var(--ink);
  }
  .roaster-info {
    position: absolute;
    top: 453px;
    left: 90px;
    font-size: 12px;
    line-height: 13.5px;
    color: var(--accent);
  }
  .roaster-info {
    top: 444px;
  }
</style>
</head>
<body>
  <main class="label-row">

    <article class="label label--gold">
      <div class="brand-mark" aria-hidden="true"></div>
      <h1 class="brand-name">Kiesel Brennerei</h1>
      <div class="product-band">Filterkaffee<br>Äthiopien – Guji</div>
      <p class="roast-level">Medium Roast</p>
      <ul class="bean-facts">
        <li>250 Gramm</li>
        <li>Helle Röstung</li>
        <li>Kaffee aus Äthiopien</li>
        <li>100% Arabica | Whashed</li>
      </ul>
      <p class="roaster-info">Geröstet in 4417 Moosbach<br>www.kiesel-brennerei.ch</p>
    </article>

    <article class="label label--rust">
      <div class="brand-mark" aria-hidden="true"></div>
      <h1 class="brand-name">Kiesel Brennerei</h1>
      <div class="product-band">Filterkaffee<br>Äthiopien – Guji</div>
      <p class="roast-level">Medium Roast</p>
      <ul class="bean-facts">
        <li>250 Gramm</li>
        <li>Helle Röstung</li>
        <li>Kaffee aus Äthiopien</li>
        <li>100% Arabica | Whashed</li>
      </ul>
      <p class="roaster-info">Geröstet in 4417 Moosbach<br>www.kiesel-brennerei.ch</p>
    </article>

    <article class="label label--umber">
      <div class="brand-mark" aria-hidden="true"></div>
      <h1 class="brand-name">Kiesel Brennerei</h1>
      <div class="product-band">Filterkaffee<br>Äthiopien – Guji</div>
      <p class="roast-level roast-level--dark">Dark Roast</p>
      <ul class="bean-facts">
        <li>250 Gramm</li>
        <li>Helle Röstung</li>
        <li>Kaffee aus Äthiopien</li>
        <li>100% Arabica | Whashed</li>
      </ul>
      <p class="roaster-info">Geröstet in 4417 Moosbach<br>www.kiesel-brennerei.ch</p>
    </article>

  </main>
</body>
</html>
```